I am a highly experienced private practice psychotherapist serving high end clientele in the Wall Street area of New York City. I need electronic letterhead (that can also be printed) to use for bills, receipts, and correspondences.

My clients are very high end and are used to elegance and wealth. The letterhead should contain the following information: Marian T. Holcombe, LCSW 72 Pellham Street, Suite 2561 New York, NY 10087 Phone : (917) 555-3194 email: therapy@marianholcombelcsw.example website: www.marianholcombelcsw.example

Thank you for your designs. Please be advised that the letterhead will be used for bills/invoices; professional letters to other mental health professionals and doctors, as well as to attorneys. It needs to be highly professional in the same way that a law firm has professional and elegant letterhead, raher than whimsical or with spa designers. My letters end up as official documents.

```html
<!DOCTYPE html>
<html lang="en">
<head>
<meta charset="utf-8">
<title>Marian T. Holcombe, LCSW — Stationery</title>
<link rel="stylesheet" href="https://fonts.googleapis.com/css2?family=Arimo:wght@400;700&family=Tinos:ital,wght@0,400;1,700&display=swap">
<style>
  :root {
    --ink: #000000;
    --paper: #ffffff;
    --teal: #7ddbd0;
    --backdrop: #e4e4e4;
    --stone-dark: #3f4a66;
    --stone-light: #c9cfdc;
    --text-light: #ffffff;
    --sans: "Arimo", Arial, sans-serif;
    --serif: "Tinos", "Times New Roman", serif;
  }
  * { box-sizing: border-box; margin: 0; padding: 0; }
  html, body { width: 927px; height: 1200px; overflow: hidden; background: var(--backdrop); }
  .sheet {
    position: absolute; left: 30px; top: 30px; width: 867px; height: 1140px;
    background: var(--paper); overflow: hidden;
    box-shadow: 0 2px 10px rgba(0,0,0,.25);
  }
  .icons { position: absolute; width: 0; height: 0; }

  /* shared identity */
  .photo-stones {
    background: radial-gradient(ellipse at 55% 60%, var(--stone-dark) 0 22%, var(--stone-light) 36%, var(--paper) 62%);
  }
  .name { font-family: var(--sans); font-weight: 700; color: var(--text-light); font-variant: small-caps; letter-spacing: .3px; white-space: nowrap; }
  .discipline { font-family: var(--serif); font-style: italic; font-weight: 700; color: var(--text-light); }
  .specialties { font-family: var(--serif); color: var(--text-light); white-space: nowrap; }
  .contact { list-style: none; font-family: var(--sans); color: var(--text-light); white-space: nowrap; }
  .contact li { display: flex; align-items: flex-start; }
  .contact svg { flex: none; fill: var(--text-light); }

  /* letterhead header */
  .letterhead-header { position: absolute; left: 0; top: 0; width: 867px; height: 170px; }
  .header-band { position: absolute; inset: 0; width: 867px; height: 170px; }
  .header-logo { position: absolute; left: 24px; top: 26px; width: 164px; height: 116px; }
  .header-id { position: absolute; left: 205px; top: 40px; }
  .header-id .name { font-size: 16px; }
  .header-id .discipline { font-size: 14px; margin-top: 4px; }
  .header-id .specialties { font-size: 15px; margin-top: 2px; }
  .header-contact { position: absolute; left: 520px; top: 24px; font-size: 13.5px; }
  .header-contact li { margin-bottom: 5px; }
  .header-contact svg { width: 16px; height: 16px; margin-right: 8px; margin-top: 1px; }

  /* envelope */
  .envelope { position: absolute; left: 100px; top: 300px; width: 660px; height: 290px; }
  .envelope-shape { position: absolute; inset: 0; }
  .envelope-logo { position: absolute; left: 40px; top: 140px; width: 60px; height: 44px; }
  .envelope-id { position: absolute; left: 106px; top: 140px; font-size: 8px; line-height: 1.2; }
  .envelope-id .name { font-size: 9px; }
  .envelope-id .discipline, .envelope-id .specialties { font-size: 8px; }
  .envelope-id .address { font-family: var(--sans); font-size: 7px; color: var(--text-light); }
  .envelope-photo {
    position: absolute; right: 0; top: 160px; width: 220px; height: 130px;
    background: linear-gradient(160deg, #000 0%, #2a2d3a 40%, #8f95a8 75%, #d6d9e2 100%);
  }

  /* business cards */
  .card { position: absolute; width: 345px; height: 210px; background: var(--ink); }
  .card-vertical { left: 455px; top: 610px; }
  .card-vertical .teal-panel { position: absolute; left: 10px; top: 0; width: 128px; height: 210px; background: var(--teal); }
  .card-vertical .card-logo { left: 28px; top: 30px; width: 97px; height: 70px; }
  .card-vertical .card-id { left: 150px; top: 30px; }
  .card-vertical .card-contact { left: 150px; top: 110px; }
  .card-horizontal { left: 85px; top: 780px; height: 190px; width: 350px; }
  .card-horizontal .divider { position: absolute; left: 130px; top: 20px; width: 1px; height: 140px; background: #8a8a8a; }
  .card-horizontal .card-logo { left: 20px; top: 78px; width: 97px; height: 70px; }
  .card-horizontal .card-id { left: 147px; top: 30px; }
  .card-horizontal .card-contact { left: 152px; top: 108px; }
  .card-logo { position: absolute; }
  .card-id { position: absolute; }
  .card-id .name { font-size: 12px; }
  .card-id .discipline { font-size: 11px; margin-top: 4px; }
  .card-id .specialties { font-size: 12px; margin-top: 2px; }
  .card-contact { position: absolute; font-size: 8.5px; }
  .card-contact li { margin-bottom: 4px; }
  .card-contact svg { width: 10px; height: 10px; margin-right: 5px; }

  /* footer */
  .footer-wave { position: absolute; left: 0; bottom: 0; width: 867px; height: 110px; }
  .footer-stones {
    position: absolute; right: 10px; bottom: 40px; width: 64px; height: 200px;
    background: linear-gradient(180deg, #6f7474 0%, #8fb7a3 50%, #5f8f76 100%);
    border-radius: 30px 30px 20px 20px;
  }
</style>
</head>
<body>
<svg class="icons" aria-hidden="true">
  <symbol id="icon-pin" viewBox="0 0 16 16"><circle cx="8" cy="8" r="8"/><path d="M8 3.5a3 3 0 0 0-3 3c0 2.2 3 5.5 3 5.5s3-3.3 3-5.5a3 3 0 0 0-3-3zm0 4.2a1.2 1.2 0 1 1 0-2.4 1.2 1.2 0 0 1 0 2.4z" fill="#000"/></symbol>
  <symbol id="icon-phone" viewBox="0 0 16 16"><circle cx="8" cy="8" r="8"/><path d="M5.6 4h1.5l.7 2-1 .8a6 6 0 0 0 2.4 2.4l.8-1 2 .7v1.5c0 .5-.4.8-.9.8A7 7 0 0 1 4.8 4.9c0-.5.3-.9.8-.9z" fill="#000"/></symbol>
  <symbol id="icon-mail" viewBox="0 0 16 16"><circle cx="8" cy="8" r="8"/><rect x="4" y="5" width="8" height="6" rx=".6" fill="#000"/><path d="M4.3 5.4 8 8.4l3.7-3" stroke="#fff" stroke-width=".8" fill="none"/></symbol>
  <symbol id="icon-web" viewBox="0 0 16 16"><circle cx="8" cy="8" r="8"/><g fill="none" stroke="#000" stroke-width=".9"><circle cx="8" cy="8" r="4.2"/><ellipse cx="8" cy="8" rx="1.8" ry="4.2"/><path d="M3.8 8h8.4M4.5 6h7M4.5 10h7"/></g></symbol>
</svg>

<main class="sheet">
  <header class="letterhead-header">
    <svg class="header-band" viewBox="0 0 867 170" aria-hidden="true">
      <rect width="867" height="156" fill="var(--ink)"/>
      <polygon points="0,156 867,156 867,171 0,171" fill="var(--paper)"/>
      <polygon points="0,156 867,145 867,156 0,170" fill="var(--teal)"/>
    </svg>
    <div class="header-logo photo-stones" role="img" aria-label="Photo of stacked smooth stones with a sprig of grass"></div>
    <div class="header-id">
      <p class="name">Marian T. Holcombe, LCSW</p>
      <p class="discipline">Psychotherapy</p>
      <p class="specialties">Individual, Family, Relationship</p>
    </div>
    <ul class="contact header-contact">
      <li><svg><use href="#icon-pin"/></svg><span>72 Pellham Street, Suite 2561<br>New York, NY 10087</span></li>
      <li><svg><use href="#icon-phone"/></svg><span>Phone : (917) 555-3194</span></li>
      <li><svg><use href="#icon-mail"/></svg><span>email: therapy@marianholcombelcsw.example</span></li>
      <li><svg><use href="#icon-web"/></svg><span>website: www.marianholcombelcsw.example</span></li>
    </ul>
  </header>

  <section class="envelope" aria-label="Envelope">
    <svg class="envelope-shape" viewBox="0 0 660 290" aria-hidden="true">
      <rect x="0" y="60" width="660" height="230" fill="var(--ink)"/>
      <polygon points="0,60 300,0 660,0 660,60" fill="var(--teal)"/>
      <polygon points="0,130 660,60 0,60" fill="var(--teal)"/>
    </svg>
    <div class="envelope-logo photo-stones" role="img" aria-label="Photo of stacked smooth stones"></div>
    <div class="envelope-id">
      <p class="name">Marian T. Holcombe, LCSW</p>
      <p class="discipline">Psychotherapy</p>
      <p class="specialties">Individual, Family, Relationship</p>
      <p class="address">72 Pellham Street, Suite 2561<br>New York, NY 10087</p>
    </div>
    <div class="envelope-photo" role="img" aria-label="Photo of stepping stones across still water"></div>
  </section>

  <section class="card card-vertical" aria-label="Business card, teal panel">
    <div class="teal-panel"></div>
    <div class="card-logo photo-stones" role="img" aria-label="Photo of stacked smooth stones"></div>
    <div class="card-id">
      <p class="name">Marian T. Holcombe, LCSW</p>
      <p class="discipline">Psychotherapy</p>
      <p class="specialties">Individual, Family, Relationship</p>
    </div>
    <ul class="contact card-contact">
      <li><svg><use href="#icon-pin"/></svg><span>72 Pellham Street, Suite 2561<br>New York, NY 10087</span></li>
      <li><svg><use href="#icon-phone"/></svg><span>Phone : (917) 555-3194</span></li>
      <li><svg><use href="#icon-mail"/></svg><span>email: therapy@marianholcombelcsw.example</span></li>
      <li><svg><use href="#icon-web"/></svg><span>website: www.marianholcombelcsw.example</span></li>
    </ul>
  </section>

  <section class="card card-horizontal" aria-label="Business card, black">
    <div class="divider"></div>
    <div class="card-logo photo-stones" role="img" aria-label="Photo of stacked smooth stones"></div>
    <div class="card-id">
      <p class="name">Marian T. Holcombe, LCSW</p>
      <p class="discipline">Psychotherapy</p>
      <p class="specialties">Individual, Family, Relationship</p>
    </div>
    <ul class="contact card-contact">
      <li><svg><use href="#icon-pin"/></svg><span>72 Pellham Street, Suite 2561<br>New York, NY 10087</span></li>
      <li><svg><use href="#icon-phone"/></svg><span>Phone : (917) 555-3194</span></li>
      <li><svg><use href="#icon-mail"/></svg><span>email: therapy@marianholcombelcsw.example</span></li>
      <li><svg><use href="#icon-web"/></svg><span>website: www.marianholcombelcsw.example</span></li>
    </ul>
  </section>

  <svg class="footer-wave" viewBox="0 0 867 110" preserveAspectRatio="none" aria-hidden="true">
    <path d="M0 110 C60 40 200 30 420 45 C600 58 760 55 867 30 L867 110 Z" fill="var(--teal)"/>
    <path d="M0 110 C70 55 210 48 420 58 C600 68 760 68 867 45 L867 110 Z" fill="var(--paper)"/>
    <path d="M0 110 C75 62 215 56 420 64 C600 74 760 76 867 52 L867 110 Z" fill="var(--ink)"/>
  </svg>
  <div class="footer-stones" role="img" aria-label="Photo of a tall stack of green-grey stones"></div>
</main>
</body>
</html>
```